Calloway Aeronautics website

We are an aviation company based in Miramar, FL but with worldwide coverage. We are involved in commercial aircraft (mostly freighters) trading, sale & leasing. Specifically, we specialized in freighters of the Vantrex family (V310, V320, V330, V340, V350). We also assist with financing, sale/leaseback. Handle special aviation projects and provide consultancy services. Currently engaged in a Vantrex 350 passenger to Freighter conversion (P2F).

Website Preliminary Initial Content/Sections as follows:

About Us
Founded in 2011, Calloway Aeronautics' management has many years of experience in Aviation, a strong background in scheduled airlines with emphasis in all cargo operations, freight forwarding supply chain and freight logistics, as well as ACMI and CMI operations.

Calloway’s focuses in facilitating wet and dry lease operations, charter and ACMI programs consultancy, aircraft sales, leasing and procurement, aviation consultancy and aircraft management.

Calloway team is a hands-on reliable alternative that works toward achieving your aircraft and aviation objectives by meeting your requirements and timeframe throughout professional and personalized service.

Teodoro Lasalle has over three decades of experience in the aviation field including aircraft maintenance, airline management, supply chain and logistics management. Teodoro is a true entrepreneur with proven experience and expertise on the multiple facets of the commercial aviation industry throughout the creation and development of a cluster of aviation entities. Teodoro is the founder and former sole member/chairman of 64 Jet, a Vantrex 340 All-Cargo U.S. Certificated Air Carrier created from scratch in 2014 which nowadays conforms a superb growing airline platform with an immaculate compliance operational record.

Services

Aircraft Finance, Trading, Procurement and Leasing
Calloway buys, sells, leases and facilitates aircraft trading while specializes in structured aircraft investment projects. Calloway has deep industry relationships and years of expertise, allowing to successfully execute lease transactions. We assist airlines, financial institutions and leasing companies when selling or purchasing aircraft.

Aircraft Available for Sale/Lease

Sale/Leaseback
Sale-leaseback is a method of financing. If your company needs liquidity, your aircraft or engine can serve as collateral for a loan throughout a sale-leaseback transaction. Sale-leaseback can free the equity tied up in aircraft or asset. Even if there is no pressing need for funds, a sale-leaseback allows you to use the equity tied up in your aircraft in a more productive fashion. Leaseback arrangements are usually employed because they confer financing, accounting or taxation benefits.

Passenger to Freighter Conversion (P2F)
Pandemic has seen the resurgence of operators packing freight into the main cabins of passenger aircraft. Carriers have been allowed to transport cargo in the cabin by removing passenger seats completely. NCA/ORSA have established exemptions that allow operators to fly in “Preighter” configuration for a limited time. Calloway is closely working with a U.S. group that is developing a Class E Supplemental Type Certificate (STC) for applicability on V350 aircraft which will include a cargo door for containerized freight. Final approvals are expected during first quarter of 2022.
Wet lease
Throughout our deep relationships within the industry, Calloway facilitates short or long-term wet leases to airlines and qualified parties around the globe, whereby we provide the Aircraft, Crews, Maintenance and Insurance (ACMI) worldwide services at competitive rates. We also specialize in AM leases where the aircraft is registered onto Lessee´s AOC with all maintenance services included in the rates, covering all maintenance risks, or CM or CMI where the client provides the aircraft.

Dry Lease
We offer aircraft from our own portfolio on dry lease or could engage in procuring the aircraft of your choice.

Asset & Aircraft Management
We provide aircraft owners Aircraft Management services, where we manage the technical side of the aircraft or the asset. Calloway also provides Harwick Dynamo engines trading, repair and full management services. We also buy Vantrex/Skylane surplus inventory.

Worldwide Charters
We facilitate the arrangement of full charters to airlines and logistics companies. Certain territory restrictions may apply.

Aviation Consultancy
We provide airline consultancy services for new or special projects. Calloway also specializes on All Cargo International route analysis, implementation and development. Our team provides professional guidance in obtaining worldwide both scheduled and charter authority.

Target Market(s)

Our target market are the airlines, logistics companies and commercial aviation related entities

Industry/Entity Type

Commercial Aviation

Coding

Number of Pages Required

3 page

Requirements
Must have
• Illustrations of wide body freighters such V350, V340, V320

```html
<!DOCTYPE html>
<html lang="en">
<head>
<meta charset="utf-8">
<title>Calloway Aeronautics</title>
<link rel="stylesheet" href="https://fonts.googleapis.com/css2?family=Cinzel:wght@400&family=Poppins:wght@300;400;500;600&display=swap">
<style>
:root{
  --navy:#0b1441;
  --ink:#1b2554;
  --muted:#8a93a6;
  --pill:#7f8ba0;
  --mist:#e4e9ef;
  --line:#b9c3d3;
  --white:#ffffff;
  --sky-top:#3f7fbf;
  --sky-mid:#8db6d8;
  --sky-low:#d9dfe3;
}
*{margin:0;padding:0;box-sizing:border-box}
html,body{width:1200px;height:4959px;overflow:hidden}
body{position:relative;background:var(--white);font-family:'Poppins',sans-serif;color:var(--muted)}
.abs{position:absolute}
.serif{font-family:'Cinzel',serif;font-weight:400}

/* hero */
.hero{left:0;top:0;width:1200px;height:640px;
  background:linear-gradient(180deg,var(--sky-top) 0%,var(--sky-mid) 40%,#c9d6df 75%,var(--sky-low) 100%);
  clip-path:polygon(0 0,100% 0,100% 578px,50% 640px,0 578px)}
.nav a{position:absolute;top:54px;font-family:'Cinzel',serif;font-size:21px;color:var(--white);text-decoration:none;letter-spacing:1px}
.nav .active{border-bottom:5px solid rgba(255,255,255,.85);padding-bottom:8px}
.brand{position:absolute;text-align:center;font-family:'Cinzel',serif;font-weight:400;color:var(--white)}
.brand .name{display:block;font-size:34px;letter-spacing:2px;line-height:1}
.brand .sub{display:block;font-size:15px;letter-spacing:14px;margin-top:8px;padding-left:14px}
.hero-title{left:0;top:196px;width:1200px;text-align:center;font-size:60px;color:var(--white);letter-spacing:3px}
.dot{width:12px;height:12px;border-radius:50%;background:#9fb2cf}

/* about */
.about-photo{left:96px;top:828px;width:444px;height:520px;
  background:linear-gradient(180deg,#b8c7d6 0%,#9aa6ad 55%,#7d7a66 100%);
  clip-path:polygon(25% 0,100% 0,100% 88%,50% 100%,0 88%,0 12%)}
.h2{font-size:50px;color:var(--ink);letter-spacing:2px}
.about-copy{left:616px;top:898px;width:470px;font-size:16.5px;line-height:27px;font-weight:300}
.about-copy p+p{margin-top:27px}
.btn{display:flex;align-items:center;justify-content:center;background:var(--navy);color:var(--white);border-radius:30px;font-family:'Cinzel',serif;font-size:21px;letter-spacing:1px}

/* services */
.services{left:0;top:1348px;width:1200px;height:1021px;background:var(--navy);
  clip-path:polygon(0 0,100% 0,100% 925px,50% 1021px,0 925px)}
.services-photo{left:0;top:0;width:1200px;height:520px;
  background:linear-gradient(180deg,#ffffff 0%,#d7dde6 30%,#7b86a2 65%,var(--navy) 100%)}
.services .h2{color:var(--white)}
.services-intro{left:190px;top:520px;width:820px;text-align:center;color:#dfe4ef;font-size:17px;line-height:27px;font-weight:300}
.svc{width:200px;text-align:center}
.svc .ring{width:144px;height:144px;margin:0 auto;border-radius:50%;background:#8a94a8;border:6px solid #b7bfcd;display:flex;align-items:center;justify-content:center}
.svc .ring.sm{width:124px;height:124px;margin-top:10px}
.svc span{display:block;margin-top:16px;color:var(--white);font-weight:600;font-size:22px}

.vline{left:599px;top:2390px;width:2px;height:75px;background:var(--ink)}

/* fleet */
.fleet-bg{left:0;top:2890px;width:1200px;height:943px;
  background:linear-gradient(180deg,#ffffff 0%,var(--mist) 40%,var(--mist) 100%);
  clip-path:polygon(0 0,100% 0,100% 855px,50% 943px,0 855px)}
.card{width:306px;height:443px;background:var(--white);box-shadow:0 2px 8px rgba(27,37,84,.12);text-align:center}
.card .ph{height:187px}
.card h3{margin:28px 18px 0;color:var(--ink);font-weight:500;font-size:19px;line-height:24px}
.card p{margin:14px 38px 0;font-size:13.5px;line-height:19px;font-weight:300;height:95px;overflow:hidden}
.card .more{position:absolute;left:84px;bottom:22px;width:136px;height:36px;border-radius:20px;background:var(--pill);color:var(--white);font-size:11.5px;font-weight:600;display:flex;align-items:center;justify-content:center}

/* contact */
.contact-sub{left:0;top:4032px;width:1200px;text-align:center;font-size:24px;line-height:30px;color:#8a94a8;font-weight:300}
.field{font-size:14px;color:#8a94a8}
.rule{height:3px;background:var(--line)}
.contact-photo{left:80px;top:4230px;width:1040px;height:240px;
  background:radial-gradient(ellipse at center,rgba(190,200,214,.55) 0%,rgba(220,226,234,.25) 45%,rgba(255,255,255,0) 70%)}

/* footer */
.footer{left:0;top:4490px;width:1200px;height:469px;background:var(--navy);
  clip-path:polygon(0 0,50% 80px,100% 0,100% 100%,0 100%)}
.info{display:flex;align-items:center;gap:16px;color:#dfe4ef;font-size:17px;line-height:26px}
.info .ico{width:50px;height:50px;border-radius:50%;background:#8a94a8;display:flex;align-items:center;justify-content:center;flex:none}
.copy{left:0;top:4906px;width:1200px;text-align:center;color:#dfe4ef;font-size:14px;letter-spacing:1.5px}
</style>
</head>
<body>

<header class="hero abs" role="img" aria-label="Wide-body freighter aircraft climbing toward the viewer against a blue sky">
</header>
<nav class="nav">
  <a class="active" style="left:112px">HOME</a>
  <a style="left:238px">ABOUT US</a>
  <a style="left:777px">SERVICES</a>
  <a style="left:938px">CONTACT US</a>
</nav>
<div class="brand" style="left:440px;top:34px;width:320px">
  <span class="name">CALLOWAY</span><span class="sub">AERONAUTICS</span>
</div>
<h1 class="hero-title abs serif">CALLOWAY AERONAUTICS</h1>
<div class="dot abs" style="left:594px;top:668px"></div>

<section>
  <div class="about-photo abs" role="img" aria-label="Front view of a wide-body jet on the runway"></div>
  <h2 class="h2 abs serif" style="left:612px;top:812px">ABOUT US</h2>
  <div class="about-copy abs">
    <p>Founded in 2011, Calloway Aeronautics' management has many years of experience in Aviation, a strong background in scheduled airlines with emphasis in all cargo operations, freight forwarding supply chain and freight logistics, as well as ACMI and CMI operations.</p>
    <p>Calloway’s focuses in facilitating wet and dry lease operations, charter and ACMI programs consultancy, aircraft sales, leasing and procurement, aviation consultancy and aircraft management.</p>
  </div>
  <div class="btn abs" style="left:616px;top:1200px;width:197px;height:58px">READ MORE</div>
</section>

<section class="services abs">
  <div class="services-photo abs" role="img" aria-label="Wide-body freighter landing on a runway at speed"></div>
  <h2 class="h2 abs serif" style="left:0;top:418px;width:1200px;text-align:center">OUR SERVICES</h2>
  <p class="services-intro abs">Calloway buys, sells, leases and facilitates aircraft trading while specializes in structured aircraft investment projects. Calloway has deep industry relationships and years of expertise, allowing to successfully execute lease transactions. We assist airlines, financial institutions and leasing companies when selling or purchasing aircraft.</p>
  <div class="svc abs" style="left:175px;top:670px">
    <div class="ring"><svg width="70" height="70" viewBox="0 0 70 70" fill="none" stroke="#0b1441" stroke-width="3"><rect x="14" y="30" width="10" height="22"/><rect x="30" y="20" width="10" height="32"/><rect x="46" y="12" width="10" height="40"/><path d="M8 56h56"/></svg></div>
    <span>Aircraft Finance</span>
  </div>
  <div class="svc abs" style="left:412px;top:670px">
    <div class="ring sm"><svg width="60" height="60" viewBox="0 0 60 60" fill="none" stroke="#0b1441" stroke-width="3"><path d="M10 50V38M22 50V30M34 50V34M46 50V22"/><path d="M10 28l12-10 10 6 16-14"/><path d="M42 10h6v6"/></svg></div>
    <span>Trading</span>
  </div>
  <div class="svc abs" style="left:651px;top:670px">
    <div class="ring sm"><svg width="60" height="60" viewBox="0 0 60 60" fill="none" stroke="#0b1441" stroke-width="3"><circle cx="30" cy="24" r="13"/><path d="M30 16v16M26 20h6a3 3 0 010 6h-4a3 3 0 000 6h6"/><path d="M8 40l12 8h20l12-8"/></svg></div>
    <span>Procurement</span>
  </div>
  <div class="svc abs" style="left:888px;top:670px">
    <div class="ring sm"><svg width="60" height="60" viewBox="0 0 60 60" fill="none" stroke="#0b1441" stroke-width="3"><circle cx="30" cy="20" r="8"/><path d="M30 28v12M30 34h6"/><path d="M8 44c8 0 12 6 22 6s14-6 22-6"/></svg></div>
    <span>Leasing</span>
  </div>
</section>
<div class="dot abs" style="left:594px;top:2352px"></div>
<div class="vline abs"></div>

<section>
  <div class="fleet-bg abs"></div>
  <h2 class="h2 abs serif" style="left:0;top:2470px;width:1200px;text-align:center;line-height:56px">AIRCRAFT AVAILABLE<br>FOR SALE/LEASE</h2>

  <article class="card abs" style="left:112px;top:2639px">
    <div class="ph" role="img" aria-label="Passenger jet taking off" style="background:linear-gradient(180deg,#dfe6ee,#b9c4d0)"></div>
    <h3>Sale/Leaseback</h3>
    <p>Sale-leaseback is a method of financing. If your company needs liquidity, your aircraft or engine can serve as collateral for a loan throughout a sale leaseback transaction.</p>
    <div class="more">READ MORE</div>
  </article>
  <article class="card abs" style="left:447px;top:2639px">
    <div class="ph" role="img" aria-label="Traveller working on a laptop in an aircraft cabin" style="background:linear-gradient(180deg,#d8d6d2,#8b8a88)"></div>
    <h3>Passenger to Freighter Conversion (P2F)</h3>
    <p>Pandemic has seen the resurgence of operators packing freight into the main cabins of passenger aircraft. Carriers have been allowed to transport</p>
    <div class="more">READ MORE</div>
  </article>
  <article class="card abs" style="left:784px;top:2639px">
    <div class="ph" role="img" aria-label="Wide-body jet parked at an airport gate" style="background:linear-gradient(180deg,#8fb4d6,#b7a99a)"></div>
    <h3>Wet lease</h3>
    <p>Throughout our deep relationships within the industry, Calloway facilitates short or long-term wet leases to airlines and qualified parties around the globe, whereby we provide.</p>
    <div class="more">READ MORE</div>
  </article>

  <article class="card abs" style="left:112px;top:3126px">
    <div class="ph" role="img" aria-label="Wide-body jet on the apron" style="background:linear-gradient(180deg,#c9d6e3,#9aa3ad)"></div>
    <h3>Dry Lease</h3>
    <p>We offer aircraft from our own portfolio on dry lease or could engage in procuring the aircraft of your choice.</p>
    <div class="more">READ MORE</div>
  </article>
  <article class="card abs" style="left:447px;top:3126px">
    <div class="ph" role="img" aria-label="Cabin crew in yellow uniforms" style="background:linear-gradient(180deg,#d9c58a,#c79a2c)"></div>
    <h3>Asset &amp; Aircraft Management</h3>
    <p>We provide aircraft owners Aircraft Management services, where we manage the technical side of the aircraft or the asset. Calloway also provides Harwick Dynamo</p>
    <div class="more">READ MORE</div>
  </article>
  <article class="card abs" style="left:784px;top:3126px">
    <div class="ph" role="img" aria-label="Jet on approach over a coastline" style="background:linear-gradient(180deg,#3f7fc2,#9ab8cc 70%,#6d8a5e)"></div>
    <h3>Worldwide Charters</h3>
    <p>We facilitate the arrangement of full charters to airlines and logistics companies. Certain territory restrictions may apply.</p>
    <div class="more">READ MORE</div>
  </article>

  <div class="btn abs" style="left:456px;top:3669px;width:287px;height:58px">VIEW ALL SERVICES</div>
</section>
<div class="dot abs" style="left:594px;top:3818px"></div>

<section>
  <h2 class="h2 abs serif" style="left:0;top:3928px;width:1200px;text-align:center">CONTACT US</h2>
  <p class="contact-sub abs">Sed ut perspiciatis unde omnis iste natus error sit<br>voluptatem accusantium doloremque laud</p>
  <div class="contact-photo abs" role="img" aria-label="Faint silhouette of a wide-body jet"></div>
  <div class="field abs" style="left:258px;top:4130px">Name:</div>
  <div class="rule abs" style="left:256px;top:4168px;width:326px"></div>
  <div class="field abs" style="left:618px;top:4130px">Email:</div>
  <div class="rule abs" style="left:618px;top:4168px;width:326px"></div>
  <div class="field abs" style="left:258px;top:4198px">Phone:</div>
  <div class="rule abs" style="left:256px;top:4235px;width:326px"></div>
  <div class="field abs" style="left:618px;top:4198px">Subject:</div>
  <div class="rule abs" style="left:618px;top:4235px;width:326px"></div>
  <div class="field abs" style="left:258px;top:4258px">Message:</div>
  <div class="btn abs" style="left:505px;top:4397px;width:190px;height:58px">SUBMIT</div>
</section>

<footer class="footer abs"></footer>
<div class="dot abs" style="left:594px;top:4585px"></div>
<div class="brand" style="left:440px;top:4686px;width:320px">
  <span class="name">CALLOWAY</span><span class="sub">AERONAUTICS</span>
</div>
<div class="info abs" style="left:233px;top:4800px">
  <div class="ico"><svg width="24" height="24" viewBox="0 0 24 24" fill="#0b1441"><path d="M6.6 10.8a15 15 0 006.6 6.6l2.2-2.2a1 1 0 011-.25 11.4 11.4 0 003.6.57 1 1 0 011 1V20a1 1 0 01-1 1A17 17 0 013 4a1 1 0 011-1h3.5a1 1 0 011 1c0 1.25.2 2.45.57 3.57a1 1 0 01-.25 1z"/></svg></div>
  <div>Phone<br>+00 4815 3390</div>
</div>
<div class="info abs" style="left:489px;top:4800px">
  <div class="ico"><svg width="24" height="24" viewBox="0 0 24 24" fill="none" stroke="#0b1441" stroke-width="2"><rect x="3" y="5" width="18" height="14" rx="1"/><path d="M3 6l9 7 9-7"/></svg></div>
  <div>Email<br>info@callowayaero.com</div>
</div>
<div class="info abs" style="left:766px;top:4800px">
  <div class="ico"><svg width="24" height="24" viewBox="0 0 24 24" fill="#0b1441"><path d="M12 2a7 7 0 00-7 7c0 5 7 13 7 13s7-8 7-13a7 7 0 00-7-7zm0 9.5A2.5 2.5 0 1112 6.5a2.5 2.5 0 010 5z"/></svg></div>
  <div>Lindqvist 9, 4400<br>Harrowby</div>
</div>
<p class="copy abs">COPYRIGHT © 2021 ALL RIGHT RESERVED</p>

</body>
</html>
```